Front cover for Bathroom Catalogue

We want to see some concepts for a new front cover of our next catalogue. Attached is the existing.

The following must be included on the cover:
1. "Corlen Vaska" logo
2. x9 product category Icons (can display just 9 or turn into a pattern like exisiting)
3. Ideally we include the Water Splash Pattern in some capacity, also attached (Feel free to add colour to the splash/edit or incorporate the splash into something else).

We also wish to add some colour/colours to make it stand out from the previous cover too.

Target Market(s)

Home owners, renovators, designers, architects

Industry/Entity Type

Bathroom

Font styles to use
Sans Serif

Colors
0054AA
0677BA
7BADD7
CADEEF
E8F1F8
0094D4
00A9DD
6FCCEA
C7EBF8
E9F6FB

Requirements
Must have
• Colour, "Corlen Vaska" logo, x9 product category icons.
Nice to have
• Possibly some colour to make it stand out.

```html
<!DOCTYPE html>
<html lang="en">
<head>
<meta charset="utf-8">
<title>Corlen Vaska – Catalogue Cover</title>
<link rel="stylesheet" href="https://fonts.googleapis.com/css2?family=Montserrat:wght@200;500&display=swap">
<style>
  :root {
    --water-deep: #1f6f86;
    --water-mid: #3a8fa6;
    --water-light: #6fb6c8;
    --water-glow: #9fd0dc;
    --towel-white: #ece9e2;
    --towel-gold: #f0a63a;
    --ink: #ffffff;
  }
  html, body {
    margin: 0;
    padding: 0;
    width: 848px;
    height: 1200px;
    overflow: hidden;
    background: var(--water-mid);
  }
  .cover {
    position: relative;
    width: 848px;
    height: 1200px;
    overflow: hidden;
    font-family: "Montserrat", sans-serif;
    color: var(--ink);
  }
  .cover__water {
    position: absolute;
    inset: 0;
    background:
      radial-gradient(ellipse 60% 45% at 48% 38%, var(--water-light) 0%, transparent 70%),
      radial-gradient(ellipse 35% 25% at 88% 65%, var(--water-glow) 0%, transparent 70%),
      linear-gradient(180deg, var(--water-mid) 0%, var(--water-deep) 45%, var(--water-mid) 75%, var(--water-light) 100%);
  }
  .cover__towel {
    position: absolute;
    left: 0;
    top: 880px;
    width: 848px;
    height: 320px;
  }
  .masthead__site {
    position: absolute;
    left: 37px;
    top: 33px;
    margin: 0;
    font-size: 16.5px;
    font-weight: 500;
    letter-spacing: 0.02em;
  }
  .masthead__issue {
    position: absolute;
    left: 37px;
    top: 60px;
    margin: 0;
    font-size: 10.5px;
    font-weight: 500;
    letter-spacing: 0.03em;
  }
  .brand {
    position: absolute;
    left: 226px;
    top: 120px;
    margin: 0;
    font-size: 84px;
    font-weight: 200;
    line-height: 1;
    letter-spacing: -0.01em;
    white-space: nowrap;
  }
  .categories {
    position: absolute;
    left: 0;
    top: 0;
    width: 848px;
    height: 1200px;
    pointer-events: none;
  }
  .categories path, .categories rect, .categories circle { fill: var(--ink); }
  .categories .outline { fill: none; stroke: var(--ink); stroke-width: 2; }
</style>
</head>
<body>
<main class="cover">
  <div class="cover__water" role="img" aria-label="Close-up photograph of rippling turquoise water"></div>
  <svg class="cover__towel" role="img" aria-label="Photograph of a folded white and yellow bath towel" viewBox="0 0 848 320" preserveAspectRatio="none">
    <defs>
      <linearGradient id="towelTone" x1="0" y1="0" x2="1" y2="1">
        <stop offset="0" stop-color="#f2eee6"/>
        <stop offset="0.35" stop-color="#f3b85a"/>
        <stop offset="0.6" stop-color="#ece8df"/>
        <stop offset="0.85" stop-color="#efb04c"/>
        <stop offset="1" stop-color="#e4e0d8"/>
      </linearGradient>
    </defs>
    <path d="M0 30 C120 10 260 0 420 20 C560 40 680 90 848 180 L848 320 L0 320 Z" fill="url(#towelTone)"/>
  </svg>

  <p class="masthead__site">HALVERDAL.CO.NZ</p>
  <p class="masthead__issue">ISSUE 25 / 2023-2024</p>
  <h1 class="brand">Corlen Vaska</h1>

  <svg class="categories" viewBox="0 0 848 1200" aria-label="Product categories">
    <!-- basin -->
    <g transform="translate(234 440)">
      <path d="M0 14 H36 V44 H22 C8 44 0 30 0 14 Z"/>
      <rect x="22" y="2" width="5" height="14"/>
      <rect x="22" y="2" width="10" height="3"/>
    </g>
    <!-- vanity -->
    <g transform="translate(418 444)">
      <rect x="0" y="0" width="36" height="40" rx="2"/>
      <rect x="6" y="8" width="24" height="4" fill="#3a8fa6" style="fill:var(--water-mid)"/>
      <rect x="6" y="22" width="24" height="4" style="fill:var(--water-mid)"/>
    </g>
    <!-- bath -->
    <g transform="translate(588 458)">
      <rect x="0" y="0" width="52" height="4" rx="1"/>
      <path d="M3 6 H49 V16 C49 20 46 22 42 22 H10 C6 22 3 20 3 16 Z"/>
      <rect x="8" y="22" width="5" height="4"/>
      <rect x="39" y="22" width="5" height="4"/>
    </g>
    <!-- basin mixer -->
    <g transform="translate(236 612)">
      <path d="M0 6 C10 0 20 2 22 4 V10 C14 8 6 10 0 12 Z"/>
      <path d="M0 18 H20 V40 H14 V24 H0 Z"/>
      <rect x="12" y="8" width="10" height="14"/>
    </g>
    <!-- toilet -->
    <g transform="translate(418 612)">
      <rect x="22" y="0" width="14" height="22" rx="2"/>
      <path d="M0 26 H36 V42 H12 C4 42 0 34 0 26 Z"/>
      <rect x="10" y="42" width="14" height="4"/>
    </g>
    <!-- hand shower -->
    <g transform="translate(598 606)">
      <circle cx="15" cy="15" r="15"/>
      <rect x="12" y="28" width="6" height="24" rx="3"/>
      <circle cx="10" cy="10" r="2" style="fill:var(--water-mid)"/>
      <circle cx="16" cy="8" r="2" style="fill:var(--water-mid)"/>
      <circle cx="21" cy="13" r="2" style="fill:var(--water-mid)"/>
      <circle cx="9" cy="17" r="2" style="fill:var(--water-mid)"/>
      <circle cx="15" cy="15" r="2" style="fill:var(--water-mid)"/>
      <circle cx="20" cy="20" r="2" style="fill:var(--water-mid)"/>
      <circle cx="14" cy="22" r="2" style="fill:var(--water-mid)"/>
    </g>
    <!-- shower enclosure -->
    <g transform="translate(236 770)">
    <path class="outline" d="M2 10 L16 2 L32 10 V44 L16 52 L2 44 Z M16 18 V52 M2 10 L16 18 L32 10"/>
      <rect x="23" y="26" width="2" height="10"/>
    </g>
    <!-- soap dispenser -->
    <g transform="translate(420 770)">
      <rect x="6" y="0" width="6" height="6"/>
      <rect x="8" y="0" width="14" height="4"/>
      <rect x="5" y="8" width="10" height="6"/>
      <rect x="2" y="14" width="24" height="30" rx="4"/>
    </g>
    <!-- kitchen mixer -->
    <g transform="translate(596 770)">
      <path class="outline" style="stroke-width:4" d="M14 52 V20 C14 4 36 4 36 20 V26"/>
      <path class="outline" style="stroke-width:2.5" d="M13 36 C6 32 2 38 8 42"/>
      <rect x="10" y="44" width="8" height="8"/>
    </g>
  </svg>
</main>
</body>
</html>
```